Cover Art for Podcast called Ahoy There Swift Otters, Badgers, Minnows!

I need this graphic to be 3000 px square at 300 DPI but it should be legible even if only 300 px square online. This will be cover Art for Podcast called Ahoy There Swift Otters, Badgers, Minnows! but may also be used on merch for the non profit featured in the show.

```html
<!DOCTYPE html>
<html lang="en">
<head>
<meta charset="utf-8">
<title>Ahoy There Swift Otters, Badgers, Minnows! — Podcast Cover</title>
<link rel="stylesheet" href="https://fonts.googleapis.com/css2?family=Poiret+One&family=Sacramento&display=swap">
<style>
  :root {
    --neon-white: #ffffff;
    --glow-warm: #f3d9a0;
    --glow-teal: #7fd6c8;
    --glow-blue: #6fa8ff;
    --glow-pink: #d070d8;
    --bg-navy: #2c3045;
    --bg-purple: #8a3590;
    --bg-rose: #8a4060;
    --bg-olive: #6f7a45;
    --bg-teal: #2a706c;
  }
  * { margin: 0; padding: 0; box-sizing: border-box; }
  html, body { width: 1200px; height: 1200px; overflow: hidden; background: var(--bg-navy); }
  .cover {
    position: relative;
    width: 1200px;
    height: 1200px;
    overflow: hidden;
    background:
      radial-gradient(circle at 0% 0%, var(--bg-purple) 0%, rgba(138,53,144,0) 38%),
      radial-gradient(circle at 100% 0%, var(--bg-rose) 0%, rgba(138,64,96,0) 42%),
      radial-gradient(circle at 6% 88%, var(--bg-olive) 0%, rgba(111,122,69,0) 38%),
      radial-gradient(circle at 95% 82%, var(--bg-teal) 0%, rgba(42,112,108,0) 40%),
      var(--bg-navy);
  }
  .frame-lines {
    position: absolute;
    inset: 0;
    width: 1200px;
    height: 1200px;
  }
  .outer-frame { stroke: var(--neon-white); stroke-width: 4; fill: none; stroke-linejoin: round; }
  .title-box {
    stroke: var(--neon-white); stroke-width: 4; fill: none;
    filter: drop-shadow(0 0 6px var(--glow-warm)) drop-shadow(0 0 14px var(--glow-warm));
  }
  .greeting {
    position: absolute;
    left: 188px;
    width: 824px;
    top: 172px;
    text-align: center;
    font-family: "Poiret One", sans-serif;
    font-size: 92px;
    letter-spacing: 10px;
    color: var(--neon-white);
    text-shadow: 0 0 6px var(--glow-teal), 0 0 16px var(--glow-teal), 0 0 28px rgba(127,214,200,0.5);
  }
  .greeting-tag {
    position: absolute;
    left: 482px;
    width: 236px;
    top: 290px;
    text-align: center;
    font-family: "Sacramento", cursive;
    font-size: 64px;
    color: var(--neon-white);
    text-decoration: underline;
    text-decoration-thickness: 3px;
    text-underline-offset: 2px;
    text-shadow: 0 0 6px var(--glow-teal), 0 0 14px var(--glow-teal);
  }
  .show-title {
    position: absolute;
    left: 40px;
    width: 1120px;
    top: 420px;
    text-align: center;
    white-space: nowrap;
    font-family: "Sacramento", cursive;
    font-size: 118px;
    line-height: 1.4;
    color: var(--neon-white);
    text-shadow: 0 0 6px var(--glow-blue), 0 0 18px var(--glow-blue), 0 0 34px rgba(111,168,255,0.55);
  }
  .mascot-art {
    position: absolute;
    left: 382px;
    top: 700px;
    width: 436px;
    height: 474px;
    border-radius: 46% 46% 8px 8px;
    background: radial-gradient(ellipse at 50% 55%, rgba(60,60,90,0.9) 0%, rgba(150,70,160,0.45) 70%, rgba(150,70,160,0) 100%);
  }
</style>
</head>
<body>
<main class="cover">
  <svg class="frame-lines" viewBox="0 0 1200 1200" aria-hidden="true">
    <path class="outer-frame" d="M419 1173 H24 V27 H1176 V1173 H753"/>
    <path class="title-box" d="M482 337 H218 Q188 337 188 307 V152 Q188 122 218 122 H982 Q1012 122 1012 152 V307 Q1012 337 982 337 H718"/>
  </svg>

  <h1 class="greeting">Ahoy There</h1>
  <p class="greeting-tag">Swift</p>
  <p class="show-title">Otters, Badgers, Minnows!</p>

  <div class="mascot-art" role="img" aria-label="Neon line illustration of two animal friends sitting side by side, outlined in white with a pink glow"></div>
</main>
</body>
</html>
```